artist "stamp" design

Im a young artist. I`m making a stamp with my information so i can make homemade business cards, so I need the following information to look good together and simple to read:

Lucila Marbán Oteiza

www.lumaroti.com

lucilamo47@vextramail.com

i want a very clan look, but with some personality. a simple logo or "look" would be great but nothing to fancy.

An idea I had was to make it look like it was written with a typewriter or a concept like that...be creative! thank you!
Updates

I don't want any image or icon, just letters, I need it to be compacto, I'm making a stamp

I don't want it to say photography 

I dont want my name to take over so it should stay close to the size as the rest of the info.

all my info should be included, this is not a logo its a design for a stamp meant to fin in a business card.

Target Market(s)

I'm a photographer, I want something very simple and I need this to make a stamp that ill use to pit on my cards and CV. I want something simple and modern

Industry/Entity Type

Business

Logo Text

Lucila Marbán Oteiza

Logo styles of interest
Abstract Logo
Wordmark Logo
Lettermark Logo
Font styles to use
Serif
Sans Serif

Requirements
Must have
• Has to look young and fresh
Nice to have
• Have to see how it looks on a business card with website and and email
Should not have
• Images

```html
<!DOCTYPE html>
<html lang="en">
<head>
<meta charset="utf-8">
<title>Lucila Marbán Oteiza — Stamp</title>
<link rel="stylesheet" href="https://fonts.googleapis.com/css2?family=Courier+Prime:ital@1&display=swap">
<style>
  :root {
    --paper: #ffffff;
    --ink: #000000;
  }
  html, body {
    margin: 0;
    width: 1200px;
    height: 1000px;
    overflow: hidden;
    background: var(--paper);
  }
  .canvas {
    position: relative;
    width: 1200px;
    height: 1000px;
  }
  .stamp {
    position: absolute;
    left: 121px;
    top: 350px;
    width: 958px;
    height: 300px;
    overflow: visible;
  }
  .stamp-frame {
    fill: none;
    stroke: var(--ink);
    stroke-width: 7;
    stroke-linejoin: miter;
  }
  .stamp-divider {
    stroke: var(--ink);
    stroke-width: 2.5;
  }
  .stamp-text {
    font-family: "Courier Prime", "Courier New", monospace;
    font-style: italic;
    font-size: 30px;
    fill: var(--ink);
    dominant-baseline: middle;
  }
</style>
</head>
<body>
  <main class="canvas">
    <svg class="stamp" viewBox="0 0 958 300" aria-label="Contact stamp for Lucila Marbán Oteiza">
      <polygon class="stamp-frame" points="299,0 958,0 659,299 0,299"/>
      <line class="stamp-divider" x1="199" y1="100" x2="858" y2="100"/>
      <line class="stamp-divider" x1="99" y1="200" x2="758" y2="200"/>
      <text class="stamp-text stamp-name" x="300" y="51">Lucila Marbán Oteiza</text>
      <text class="stamp-text stamp-web" x="208" y="151">W: www.lumaroti.com</text>
      <text class="stamp-text stamp-email" x="112" y="251">E: lucilamo47@vextramail.com</text>
    </svg>
  </main>
</body>
</html>
```